its a new company based in Christchurch new Zealand building computers ,repairs, upgrades and anything computers for the general public,i like bright happy colours like yellows, greens reds anything that stands out and it needs to communicant trust and security towards my new company,i have no logo yet,

Target Market(s)

target market of all ages

Industry/Entity Type

Building

Contact Information for Business Card

Pixel Harbour Limited,ph-0214862735,email-bluefoxtrail17@mailnest.example,4c marlowe rd,fernvale

```html
<!DOCTYPE html>
<html lang="en">
<head>
<meta charset="utf-8">
<title>Pixel Harbour Limited — Business Card</title>
<link rel="stylesheet" href="https://fonts.googleapis.com/css2?family=Libre+Baskerville:wght@400;700&display=swap">
<style>
  :root {
    --backdrop: #fdf2b0;
    --card-black: #0c0c0c;
    --card-sheen: #262626;
    --gold: #f3d21c;
    --signal-red: #e2262d;
    --mark-grey: #4b4b4b;
  }
  * { box-sizing: border-box; margin: 0; padding: 0; }
  html, body {
    width: 1200px;
    height: 900px;
    overflow: hidden;
    background: var(--backdrop);
  }
  .stage {
    width: 1200px;
    height: 900px;
    display: flex;
    align-items: center;
    justify-content: center;
  }
  .business-card {
    position: relative;
    width: 840px;
    height: 480px;
    background: linear-gradient(135deg, var(--card-black) 0%, var(--card-sheen) 45%, var(--card-black) 100%);
    box-shadow: 0 18px 40px rgba(90, 70, 0, 0.25);
    font-family: "Libre Baskerville", Georgia, serif;
    color: var(--gold);
  }
  .card-frame {
    position: absolute;
    inset: 22px;
    border: 2px solid var(--gold);
  }
  .brand-mark {
    position: absolute;
    left: 268px;
    top: 70px;
    width: 150px;
    height: 110px;
    border-radius: 14px;
    background: var(--mark-grey);
    border: 2px solid var(--gold);
  }
  .company-name {
    position: absolute;
    left: 96px;
    right: 96px;
    top: 212px;
    padding-bottom: 10px;
    border-bottom: 2px solid var(--gold);
    font-size: 40px;
    font-weight: 700;
    letter-spacing: 0.5px;
    text-transform: uppercase;
    text-align: center;
    white-space: nowrap;
  }
  .contact-item {
    position: absolute;
    display: flex;
    align-items: center;
    gap: 10px;
    font-size: 18px;
    font-weight: 400;
  }
  .contact-item svg { width: 16px; height: 16px; flex: none; }
  .contact-phone { left: 104px; top: 300px; }
  .contact-email { left: 430px; top: 300px; }
  .contact-address { left: 430px; top: 346px; text-transform: capitalize; }
</style>
</head>
<body>
<main class="stage">
  <article class="business-card">
    <div class="card-frame"></div>
    <div class="brand-mark" aria-hidden="true"></div>
    <h1 class="company-name">Pixel Harbour Limited</h1>

    <p class="contact-item contact-phone">
      <svg viewBox="0 0 16 16" aria-hidden="true"><path fill="var(--signal-red)" d="M4 1 6.5 4.5 5 6.2c.8 1.9 2.6 3.7 4.6 4.6l1.6-1.5L15 11.8 13.4 15C7 14.4 1.6 9 1 2.6z"/></svg>
      0214862735
    </p>
    <p class="contact-item contact-email">
      <svg viewBox="0 0 16 16" aria-hidden="true"><rect x="1" y="3" width="14" height="10" fill="var(--signal-red)"/><path d="M1 3 8 9 15 3" fill="none" stroke="var(--card-black)" stroke-width="1.4"/></svg>
      bluefoxtrail17@mailnest.example
    </p>
    <p class="contact-item contact-address">
      <svg viewBox="0 0 16 16" aria-hidden="true"><path fill="var(--signal-red)" d="M8 1 15 8H13v7H3V8H1z"/></svg>
      4c marlowe rd, fernvale
    </p>
  </article>
</main>
</body>
</html>
```